New Zealand Luggage Importer Needs Business Cards

We need professional, creative and fashionable business cards created.
We are based in New Zealand and import and distribute high-end, quality, fashionable and durable luggage.
We pride ourselves on selling the very best quality luggage, second only to 1 brand (which we won't mention here)...we use the same manufacturer. However, our prices are much more reasonable.
Industry/Entity Type
Business
Contact Information for Business Card
Mark Dunsley
027 512 4068
3/17 Harlow Street, Pinecrest Flats, Auckland, 0614
PO Box 204377, Fernside, Auckland 0731
09-528-3916
sales@brivancases.co.nz / www.brivancases.co.nz

```html
<!DOCTYPE html>
<html lang="en">
<head>
<meta charset="utf-8">
<title>Brivan Cases – Business Cards</title>
<link rel="stylesheet" href="https://fonts.googleapis.com/css2?family=Roboto:wght@300;400;500;700&display=swap">
<style>
  :root {
    --stage: #5b646b;
    --card: #141414;
    --gold: #c9a24a;
    --white: #f4f4f4;
    --muted: #b9b9b9;
  }
  * { margin: 0; padding: 0; box-sizing: border-box; }
  html, body {
    width: 1200px; height: 900px; overflow: hidden;
    background: var(--stage);
    font-family: "Roboto", Arial, sans-serif;
  }
  .stage {
    width: 1200px; height: 900px;
    display: flex; flex-direction: column;
    align-items: center; justify-content: center; gap: 48px;
  }
  .card {
    position: relative;
    width: 620px; height: 354px;
    background: var(--card);
    border-radius: 3px;
    box-shadow: 0 14px 36px rgba(0,0,0,.45);
    overflow: hidden;
  }
  .wordmark {
    color: var(--white);
    font-weight: 700;
    letter-spacing: .08em;
    text-transform: uppercase;
    white-space: nowrap;
  }

  /* Front */
  .card-front .wordmark {
    position: absolute; left: 50%; top: 138px;
    transform: translateX(-50%);
    font-size: 52px;
  }
  .card-front .site {
    position: absolute; left: 40px; bottom: 34px;
    font-size: 14px; color: var(--muted); letter-spacing: .02em;
  }

  /* Back */
  .card-back .wordmark {
    position: absolute; right: 40px; top: 40px;
    font-size: 30px;
  }
  .name-tab {
    position: absolute; left: 0; top: 104px;
    width: 8px; height: 40px;
    background: var(--gold);
    border-radius: 0 4px 4px 0;
  }
  .person { position: absolute; left: 32px; top: 102px; }
  .person .name { font-size: 24px; font-weight: 700; color: var(--gold); line-height: 1.1; }
  .person .role { font-size: 12px; color: var(--muted); margin-top: 2px; }

  .contacts {
    position: absolute; left: 32px; top: 178px;
    list-style: none;
  }
  .contacts li {
    display: flex; align-items: center; gap: 10px;
    font-size: 13px; color: var(--white); line-height: 22px;
  }
  .contacts svg { width: 12px; height: 12px; fill: var(--gold); flex: none; }

  .address {
    position: absolute; right: 40px; bottom: 34px;
    text-align: right; font-size: 13px; color: var(--white); line-height: 19px;
    font-style: normal;
  }
  .address p + p { margin-top: 6px; }
</style>
</head>
<body>
<main class="stage">

  <section class="card card-back" aria-label="Business card, contact side">
    <div class="wordmark">Brivan Cases</div>
    <span class="name-tab"></span>
    <div class="person">
      <div class="name">Mark Dunsley</div>
      <div class="role">Owner</div>
    </div>
    <ul class="contacts">
      <li>
        <svg viewBox="0 0 12 12" aria-hidden="true"><path d="M2.4 0.6 4.3 2.5 3.3 4.1c.7 1.6 2 2.9 3.6 3.6l1.6-1 1.9 1.9-1.3 1.8C5 10.2 1.8 7 1.6 2z"/></svg>
        027 512 4068
      </li>
      <li>
        <svg viewBox="0 0 12 12" aria-hidden="true"><path d="M3 0h6a1 1 0 0 1 1 1v10a1 1 0 0 1-1 1H3a1 1 0 0 1-1-1V1a1 1 0 0 1 1-1zm0.4 1.4v8h5.2v-8z"/></svg>
        09-528-3916
      </li>
      <li>
        <svg viewBox="0 0 12 12" aria-hidden="true"><path d="M0 2h12v8H0zm1.2 1.2v.3L6 6.6l4.8-3.1v-.3zm0 1.7v3.9h9.6V4.9L6 8z"/></svg>
        sales@brivancases.co.nz
      </li>
      <li>
        <svg viewBox="0 0 12 12" aria-hidden="true"><path d="M6 0a6 6 0 1 0 0 12A6 6 0 0 0 6 0zm0 1.3a4.7 4.7 0 1 1 0 9.4 4.7 4.7 0 0 1 0-9.4zM5.4 2.8v3.6l2.8 1.7.6-1-2.2-1.3v-3z"/></svg>
        www.brivancases.co.nz
      </li>
    </ul>
    <address class="address">
      <p>3/17 Harlow Street, Pinecrest Flats<br>Auckland, 0614</p>
      <p>PO Box 204377, Fernside<br>Auckland 0731</p>
    </address>
  </section>

  <section class="card card-front" aria-label="Business card, front side">
    <div class="wordmark">Brivan Cases</div>
    <div class="site">www.brivancases.co.nz</div>
  </section>

</main>
</body>
</html>
```